Veranta - Solution provider in business consulting

Veranta is a swiss based company providing solutions for developing markets. The business covers various fields of business consulting, such as supply chain, product costs, quality management and manufacturing management. The Business operates in a efficient, straight and solution oriented manner.
The final design should communicate these characteristics. Asian people as well as as western people shall identify the qualities of the company at first sight.
The customer needs business cards with a simple view but an recognizable design, printed in high quality. Engraved elements such as the globe or simple words are possible.
Available colors are: (RAL)
102/102/102
51/102/102
153/204/153
255/102/51
Font: Calibri
Industry/Entity Type
Business
Look and feel
Each slider illustrates characteristics of the customer's brand and the style your logo design should communicate.

```html
<!DOCTYPE html>
<html lang="en">
<head>
<meta charset="utf-8">
<title>Veranta – Business Cards</title>
<link rel="stylesheet" href="https://fonts.googleapis.com/css2?family=Carlito:wght@400;700&display=swap">
<style>
  :root {
    --backdrop: #d8c7ad;
    --card-front: #eeedeb;
    --card-back: #8f8e8c;
    --brand-grey: #666666;
    --mark-grey: #5a5a5a;
    --foil: #ffffff;
    --foil-soft: #f2f2f2;
  }
  * { margin: 0; padding: 0; box-sizing: border-box; }
  html, body {
    width: 1200px;
    height: 795px;
    overflow: hidden;
    background: var(--backdrop);
    font-family: "Carlito", "Calibri", sans-serif;
  }
  .canvas {
    position: relative;
    width: 1200px;
    height: 795px;
    display: flex;
    align-items: center;
    justify-content: center;
    gap: 60px;
  }
  .card {
    width: 540px;
    height: 315px;
    position: relative;
    box-shadow: 0 6px 14px rgba(60, 45, 25, 0.25);
  }
  .card--front {
    background: var(--card-front);
    display: flex;
    align-items: center;
    justify-content: center;
  }
  .wordmark {
    display: flex;
    align-items: center;
    gap: 14px;
  }
  .wordmark__dot {
    width: 40px;
    height: 40px;
    border-radius: 50%;
    background: var(--mark-grey);
  }
  .wordmark__name {
    font-size: 54px;
    font-weight: 400;
    letter-spacing: 2px;
    color: var(--brand-grey);
    text-transform: lowercase;
  }
  .card--back {
    background: var(--card-back);
    color: var(--foil);
  }
  .card__mark {
    position: absolute;
    top: 34px;
    right: 40px;
    width: 74px;
    height: 74px;
    border-radius: 50%;
    background: var(--mark-grey);
  }
  .contact {
    position: absolute;
    left: 40px;
    bottom: 28px;
  }
  .contact__name {
    font-size: 24px;
    font-weight: 700;
    line-height: 1.1;
  }
  .contact__role {
    font-size: 14px;
    color: var(--foil-soft);
    margin-bottom: 16px;
  }
  .contact__line {
    font-size: 15px;
    line-height: 19px;
    color: var(--foil-soft);
    display: flex;
    align-items: center;
    gap: 8px;
  }
  .contact__line--spaced { margin-top: 2px; }
  .contact__icon {
    width: 13px;
    height: 13px;
    flex: none;
  }
</style>
</head>
<body>
<main class="canvas">
  <section class="card card--front" aria-label="Card front">
    <div class="wordmark">
      <span class="wordmark__name">veranta</span>
      <span class="wordmark__dot" aria-hidden="true"></span>
    </div>
  </section>

  <section class="card card--back" aria-label="Card back">
    <span class="card__mark" aria-hidden="true"></span>
    <div class="contact">
      <p class="contact__name">Marco Lenz</p>
      <p class="contact__role">CEO</p>
      <p class="contact__line">Veranta GmbH</p>
      <p class="contact__line">Lindenweg 14, 8400 Talbach</p>
      <p class="contact__line">Switzerland</p>
      <p class="contact__line contact__line--spaced">
        <svg class="contact__icon" viewBox="0 0 16 16" aria-hidden="true"><path fill="#fff" d="M3.5 1.5l2.5 0 1 3.5-1.8 1.2a9 9 0 0 0 4.6 4.6L11 9l3.5 1v2.5c0 1-1 2-2 2C6.5 14.5 1.5 9.5 1.5 3.5c0-1 1-2 2-2z"/></svg>
        +41 71 555 0182
      </p>
      <p class="contact__line">
        <svg class="contact__icon" viewBox="0 0 16 16" aria-hidden="true"><rect x="4" y="1" width="8" height="14" rx="1.5" fill="none" stroke="#fff" stroke-width="1.6"/><circle cx="8" cy="12.3" r="0.9" fill="#fff"/></svg>
        +41 79 555 0147
      </p>
      <p class="contact__line">
        <svg class="contact__icon" viewBox="0 0 16 16" aria-hidden="true"><rect x="1.5" y="3.5" width="13" height="9" fill="none" stroke="#fff" stroke-width="1.5"/><path d="M1.5 3.5L8 9l6.5-5.5" fill="none" stroke="#fff" stroke-width="1.5"/></svg>
        marco.lenz@veranta.ch
      </p>
      <p class="contact__line">
        <svg class="contact__icon" viewBox="0 0 16 16" aria-hidden="true"><circle cx="8" cy="8" r="6.5" fill="none" stroke="#fff" stroke-width="1.4"/><path d="M1.5 8h13M8 1.5c-3 3.5-3 9.5 0 13M8 1.5c3 3.5 3 9.5 0 13" fill="none" stroke="#fff" stroke-width="1.1"/></svg>
        www.veranta.ch
      </p>
    </div>
  </section>
</main>
</body>
</html>
```